Printed Promo Flyer for new pet business

We need a double sided flyer design as per the given example flyer, just better looking and more fun.Flyers will need to be printed.Flyer size approx 10.5cm x 15cm. The text will need to be amended slightly afterwards to be more fun unless you can create a new tone of voice as well (should sound fun like breezy do it) Look and Feel: emotional, fun, loving, professional
See attached files.

Target Market(s)

Pet owners in the UK who want the convenience of getting their pets parasite treatment delivered to their door without the need of having to run to the vet or store for purchase

Industry/Entity Type

Pet Care

Colors
00a990
6b449b

Requirements
Must have
• all the content context as given in the example flyer.
Nice to have
• Tone of voice can be changed to be more fun (using Breezy as a guide)

```html
<!DOCTYPE html>
<html lang="en">
<head>
<meta charset="utf-8">
<title>Tickly Tote – Flyer</title>
<link href="https://fonts.googleapis.com/css2?family=Fira+Sans:ital,wght@0,300;0,400;0,600;1,300;1,600;1,800;1,900&family=Fira+Sans+Condensed:wght@500;600&display=swap" rel="stylesheet">
<style>
  :root {
    --stage: #e4e4e2;
    --paper: #ffffff;
    --teal: #2e9db0;
    --purple: #6e5396;
    --brand-purple: #6b449b;
    --yellow: #fff200;
    --yellow-dark: #d9cc00;
    --ink: #1c1c1c;
    --white: #ffffff;
    --art-warm: #b98a55;
    --art-cool: #9a9aa6;
  }
  * { box-sizing: border-box; margin: 0; padding: 0; }
  html, body { width: 1200px; height: 802px; overflow: hidden; }
  body {
    background: var(--stage);
    font-family: "Fira Sans", sans-serif;
    position: relative;
  }
  .card {
    position: absolute;
    width: 464px;
    height: 664px;
    overflow: hidden;
    box-shadow: 0 2px 8px rgba(0,0,0,0.25);
  }
  /* Front */
  .front { left: 138px; top: 63px; background: var(--paper); }
  .front__band {
    position: absolute; left: 0; top: 363px; width: 100%; height: 301px;
    background: var(--teal);
  }
  .brand {
    position: absolute; left: 0; top: 120px; width: 100%;
    display: flex; align-items: center; justify-content: center; gap: 12px;
  }
  .brand__dot { width: 22px; height: 22px; border-radius: 50%; background: var(--teal); }
  .brand__name {
    font-family: "Fira Sans", sans-serif; font-weight: 600;
    font-size: 44px; letter-spacing: 1px; color: var(--brand-purple);
  }
  .pets-art {
    position: absolute; left: 76px; top: 275px; width: 316px; height: 122px;
    border-radius: 40px 40px 10px 10px;
    background: linear-gradient(90deg, var(--art-cool) 0%, var(--art-cool) 38%, var(--art-warm) 48%, var(--art-warm) 100%);
  }
  .tagline {
    position: absolute; left: 38px; top: 425px; color: var(--white);
  }
  .tagline__lead {
    font-weight: 300; font-style: italic; font-size: 30px; line-height: 29px; letter-spacing: 0.5px;
  }
  .tagline__big {
    margin-top: 6px; margin-left: -4px;
    font-weight: 900; font-style: italic; font-size: 62px; line-height: 66px; letter-spacing: -1px;
  }
  .tagline__big em { font-style: italic; color: var(--yellow); }

  /* Back */
  .back { left: 648px; top: 62px; background: var(--teal); }
  .back__top {
    position: absolute; left: 0; top: 0; width: 100%; height: 420px; background: var(--purple);
  }
  .heading {
    position: absolute; left: 44px; font-style: italic; font-weight: 800; font-size: 30px;
  }
  .heading--why { top: 20px; color: var(--yellow); }
  .heading--how { top: 432px; color: var(--white); font-size: 31px; }
  .benefit { position: absolute; left: 40px; display: flex; gap: 13px; color: var(--white); }
  .benefit__icon { width: 36px; height: 36px; flex: none; }
  .benefit__title { font-style: italic; font-weight: 800; font-size: 18px; line-height: 20px; }
  .benefit__text { font-weight: 400; font-size: 14.5px; line-height: 19.5px; letter-spacing: 0.4px; }
  .offer { position: absolute; left: 46px; top: 356px; display: flex; align-items: center; gap: 14px; }
  .offer__label { color: var(--white); font-style: italic; font-weight: 800; font-size: 31px; }
  .offer__box { position: relative; width: 132px; height: 66px; }
  .offer__price {
    position: absolute; left: 0; top: 0; width: 112px; height: 66px;
    background: var(--yellow); color: var(--ink);
    font-size: 38px; font-weight: 400; line-height: 66px; text-align: center;
  }
  .offer__box svg { position: absolute; left: 0; top: -18px; }
  .steps { position: absolute; left: 42px; top: 474px; list-style: none; }
  .step { display: flex; align-items: center; gap: 10px; height: 34.5px; color: var(--white);
    font-family: "Fira Sans Condensed", sans-serif; font-weight: 600; font-size: 16px; }
  .step__num {
    width: 30px; height: 30px; border-radius: 50%; background: var(--purple); border: 2px solid var(--white);
    display: flex; align-items: center; justify-content: center; font-size: 14px;
    box-shadow: 2px 3px 3px rgba(0,0,0,0.25);
  }
  .web { position: absolute; left: 0; top: 628px; width: 100%; text-align: center;
    color: var(--white); font-size: 17px; letter-spacing: 0.8px; font-weight: 400; }
</style>
</head>
<body>
  <section class="card front">
    <div class="front__band"></div>
    <div class="brand">
      <span class="brand__dot"></span>
      <span class="brand__name">TICKLY TOTE</span>
    </div>
    <div class="pets-art" role="img" aria-label="Illustration of a grey tabby cat and a brown dog peeking over the edge"></div>
    <div class="tagline">
      <p class="tagline__lead">The Best<br>Protection and Care</p>
      <p class="tagline__big">FOR <em>YOUR PET</em></p>
    </div>
  </section>

  <section class="card back">
    <div class="back__top"></div>
    <h2 class="heading heading--why">Why Tickly Tote?</h2>

    <div class="benefit" style="top:92px">
      <svg class="benefit__icon" viewBox="0 0 36 36" fill="#fff" stroke="#fff" stroke-width="2" stroke-linecap="round">
        <circle cx="18" cy="20" r="9" stroke="none"/>
        <circle cx="18" cy="9" r="3.5" stroke="none"/>
        <path d="M9 16 3 13M9 21H2M10 26 4 30M27 16l6-3M27 21h7M26 26l6 4" fill="none"/>
      </svg>
      <div><p class="benefit__title">Protection &amp; Care</p>
        <p class="benefit__text">Protection against all major parasites<br>to avoid putting your pet and family at risk</p></div>
    </div>
    <div class="benefit" style="top:164px">
      <svg class="benefit__icon" viewBox="0 0 36 36" fill="none" stroke="#fff" stroke-width="2.5" stroke-linecap="round">
        <circle cx="18" cy="18" r="15"/><path d="M18 9v9l-6 5"/>
      </svg>
      <div><p class="benefit__title">In Time</p>
        <p class="benefit__text">Never having to remember when to treat your pet</p></div>
    </div>
    <div class="benefit" style="top:214px">
      <svg class="benefit__icon" viewBox="0 0 36 36" fill="#fff">
        <path d="M2 10h24a8 8 0 0 1 8 8v2H2z"/><rect x="13" y="20" width="4" height="16"/>
        <rect x="15" y="3" width="2" height="8"/><rect x="15" y="3" width="6" height="3"/>
      </svg>
      <div><p class="benefit__title">Convenient</p>
        <p class="benefit__text">Delivered directly to your letter box</p></div>
    </div>
    <div class="benefit" style="top:264px">
      <svg class="benefit__icon" viewBox="0 0 36 36">
        <circle cx="18" cy="18" r="16" fill="#fff"/>
        <text x="18" y="25" text-anchor="middle" font-family="Fira Sans, sans-serif" font-size="20" fill="#6e5396">£</text>
      </svg>
      <div><p class="benefit__title">Low cost</p>
        <p class="benefit__text">All the high end, trusted brands<br>but cheaper than the vet</p></div>
    </div>

    <div class="offer">
      <span class="offer__label">First Box</span>
      <div class="offer__box">
        <svg width="132" height="84" viewBox="0 0 132 84">
          <polygon points="0,18 18,0 130,0 112,18" fill="#fff200" stroke="#d9cc00" stroke-width="1"/>
          <polygon points="112,18 130,0 130,66 112,84" fill="#d9cc00"/>
        </svg>
        <div class="offer__price">£5.99</div>
      </div>
    </div>

    <h2 class="heading heading--how">How it works</h2>
    <ol class="steps">
      <li class="step"><span class="step__num">1</span>Select which pet the treatment is for</li>
      <li class="step"><span class="step__num">2</span>Choose your treatment type</li>
      <li class="step"><span class="step__num">3</span>Select your preferred brand</li>
      <li class="step"><span class="step__num">4</span>Choose between 1, 3, 6 or 12 month treatment box.</li>
    </ol>
    <p class="web">www.ticklytote.co.uk</p>
  </section>
</body>
</html>
```